Online trading school - Website design

We are building an online trading school (trading of shares, commodities, indices, currencies). The purpose is to teach online traders how to trade successfully. We need to design the homepage of the website and logo (bramwelloq.com will be the domain). The homepage will contain the following elements

- logo
- Sign in and Register links/buttons
- upper menu
- short introduction
- a couple of bullet points 'Why to join our school?'
- sign up form
- text
- bottom menu

Attached is a draft for the designer. The draft is just for an inspiration, the actual structure of the website can be different if the designer thinks so.

The designer is free to choose colors.

School

3 page

```html
<!DOCTYPE html>
<html lang="en">
<head>
<meta charset="utf-8">
<title>Bramwelloq – Online Trading School</title>
<link href="https://fonts.googleapis.com/css2?family=Barlow+Semi+Condensed:wght@400;500;600;700&family=Lato:ital,wght@0,400;0,700;1,400&display=swap" rel="stylesheet">
<style>
:root{
  --navy:#0e4677;
  --navy-dark:#0b3a63;
  --green:#17a04a;
  --green-dark:#128a3e;
  --ink:#4a4a4a;
  --muted:#8a8a8a;
  --line:#dcdcdc;
  --tab:#f2f3f5;
  --white:#ffffff;
  --orange:#ef7d1a;
}
*{box-sizing:border-box;margin:0;padding:0}
html,body{width:1200px;height:2586px;overflow:hidden;background:var(--white)}
body{position:relative;font-family:"Lato",Arial,sans-serif;color:var(--ink)}
.abs{position:absolute}
.head-font{font-family:"Barlow Semi Condensed","Arial Narrow",sans-serif}

/* top bar */
.social{left:87px;top:17px;display:flex;gap:6px}
.social span{width:26px;height:26px;border:2px solid #333;border-radius:50%;display:block}
.account{right:94px;top:20px;font-size:15px;color:#333;display:flex;gap:18px}
.brand{left:0;width:1200px;top:48px;display:flex;justify-content:center;align-items:center;gap:12px}
.brand-dot{width:46px;height:46px;border-radius:50%;background:var(--navy)}
.brand-name{font-family:"Barlow Semi Condensed",sans-serif;font-weight:600;font-size:44px;color:var(--navy);letter-spacing:.5px}

/* nav */
.nav{left:87px;width:1019px;top:162px;height:64px;border-top:1px solid var(--navy);border-bottom:1px solid var(--navy)}
.nav ul{list-style:none;display:flex;justify-content:center;gap:48px;height:100%;align-items:center}
.nav li{font-family:"Barlow Semi Condensed",sans-serif;font-size:21px;font-weight:500;color:var(--navy);letter-spacing:.4px;position:relative}
.nav li.active::before{content:"";position:absolute;left:0;right:0;top:-21px;height:2px;background:var(--navy)}

/* hero */
.hero{left:87px;top:226px;width:1019px;height:499px;background:linear-gradient(160deg,#f1efec 0%,#dcd8d2 45%,#b9a894 75%,#8a7b6b 100%)}
.hero-caption{left:87px;top:607px;width:1019px;height:118px;background:rgba(12,12,12,.88)}
.hero-caption p{position:absolute;left:32px;top:30px;color:#fff;font-family:"Barlow Semi Condensed",sans-serif;font-size:25px;line-height:28px;font-weight:500;letter-spacing:.3px}
.hero-arrows{right:94px;top:607px;display:flex;height:118px}
.hero-arrows span{width:47px;height:118px;display:flex;align-items:center;justify-content:center;background:rgba(40,40,40,.9);margin-left:1px}

/* page frame */
.frame{left:87px;top:725px;width:1019px;height:1654px;border-left:1px solid #ececec;border-right:1px solid #ececec}

/* section tags */
.tag{height:39px;background:var(--tab);border-left:7px solid var(--navy);display:flex;align-items:center;padding-left:24px;font-family:"Barlow Semi Condensed",sans-serif;font-weight:600;font-size:24px;color:var(--navy);letter-spacing:.5px}
.copy{font-size:12.5px;line-height:18px;color:#555}
.btn{display:flex;align-items:center;justify-content:center;font-family:"Barlow Semi Condensed",sans-serif;font-weight:600;color:#fff;letter-spacing:.4px}
.btn-green{background:var(--green)}
.btn-navy{background:var(--navy)}

/* about */
.about-photo{left:638px;top:806px;width:427px;height:243px;background:linear-gradient(135deg,#3a3b2c 0%,#5a5a4a 45%,#8c8a80 70%,#454638 100%)}

/* banner */
.banner{left:87px;top:1121px;width:1019px;height:345px;background:linear-gradient(180deg,#7d7a76 0%,#5a5856 40%,#3a3634 100%)}
.banner h2{position:absolute;left:0;right:0;top:98px;text-align:center;color:#fff;font-family:"Barlow Semi Condensed",sans-serif;font-weight:700;font-size:36px;line-height:41px;letter-spacing:.3px}
.join-outline{left:497px;top:1325px;width:197px;height:51px;border:2px solid #fff;color:#fff;font-family:"Barlow Semi Condensed",sans-serif;font-size:30px;display:flex;align-items:center;justify-content:center;letter-spacing:1px}

/* cards */
.card{top:1625px;width:286px;height:286px;border:1px solid var(--line);background:#fff}
.card.active{border-color:var(--navy)}
.card-head{display:flex;align-items:center;height:51px}
.card-num{width:51px;height:51px;background:var(--navy);color:#fff;font-family:"Barlow Semi Condensed",sans-serif;font-weight:700;font-size:24px;display:flex;align-items:center;justify-content:center}
.card-title{margin-left:14px;font-family:"Barlow Semi Condensed",sans-serif;font-weight:500;font-size:21px;color:var(--navy);letter-spacing:.3px}
.card .copy{padding:28px 20px 0 20px;text-align:center;font-size:12px;line-height:17.6px}
.card-btn{position:absolute;left:86px;top:232px;width:104px;height:34px;font-size:12px}
.card-btn.outline{background:#fff;color:var(--navy);border:2px solid var(--navy)}

/* why join */
.bullets{left:127px;top:2154px;width:400px;display:grid;grid-template-columns:190px 200px;row-gap:10px;font-size:11.5px;line-height:14px;color:#555;list-style:none}
.bullets li{position:relative;padding-left:16px}
.bullets li::before{content:"";position:absolute;left:0;top:4px;width:7px;height:7px;border-radius:50%;background:var(--navy)}

/* form */
.form-box{left:651px;top:1982px;width:415px;height:346px;border:1px solid var(--line);background:#fff}
.form-head{height:54px;background:var(--green);color:#fff;font-family:"Barlow Semi Condensed",sans-serif;font-weight:600;font-size:22px;display:flex;align-items:center;padding-left:27px;letter-spacing:.4px}
.field{position:absolute;left:39px;width:335px;height:35px;background:#f4f4f4;border:1px solid #e6e6e6;font-size:12.5px;font-style:italic;color:#aaa;padding-left:16px;display:flex;align-items:center}
.agree{position:absolute;left:39px;top:234px;display:flex;align-items:center;gap:14px;font-size:11px;color:#bbb}
.agree i{width:15px;height:15px;border:1px solid #ccc;display:block}
.agree b{font-weight:400;color:var(--orange)}
.submit{position:absolute;left:39px;top:267px;width:335px;height:38px;background:linear-gradient(180deg,#6a6a6a,#2e2e2e);color:#fff;font-family:"Barlow Semi Condensed",sans-serif;font-weight:600;font-size:21px;display:flex;align-items:center;justify-content:center;letter-spacing:.5px}

/* footer */
.footer{left:87px;top:2379px;width:1019px;height:120px;background:var(--green)}
.footer-brand{position:absolute;left:40px;top:38px;display:flex;align-items:center;gap:10px}
.footer-brand .brand-dot{width:40px;height:40px;background:#fff}
.footer-brand .brand-name{color:#fff;font-size:36px}
.footer-links{position:absolute;left:568px;top:50px;font-size:12.5px;color:#fff;font-weight:700;display:flex;gap:18px}
.footer-social{position:absolute;right:40px;top:40px;display:flex;gap:14px}
.footer-social span{width:40px;height:40px;border:2px solid rgba(255,255,255,.45);border-radius:50%;display:block}
</style>
</head>
<body>

<header>
  <div class="abs social" aria-label="Social links"><span></span><span></span><span></span></div>
  <div class="abs account"><span>Login</span><span>|</span><span>Register</span></div>
  <div class="abs brand"><span class="brand-dot"></span><span class="brand-name">Bramwelloq</span></div>
  <nav class="abs nav">
    <ul>
      <li class="active">HOME</li>
      <li>ABOUT OUR SCHOOL</li>
      <li>RISK WARNING</li>
      <li>TRADING GLOSSARY</li>
      <li>FAQ</li>
      <li>CONTACT US</li>
    </ul>
  </nav>
</header>

<section>
  <div class="abs hero" role="img" aria-label="Photo of a man in a checked shirt reading a book beside a laptop in a bright office"></div>
  <div class="abs hero-caption"><p>TOP COMPANY DELIVERING HIGH QUALITY SERVICES<br>AROUND THE GLOBE</p></div>
  <div class="abs hero-arrows">
    <span><svg width="14" height="22" viewBox="0 0 14 22"><path d="M11 2 3 11l8 9" fill="none" stroke="#fff" stroke-width="2.5"/></svg></span>
    <span><svg width="14" height="22" viewBox="0 0 14 22"><path d="M3 2l8 9-8 9" fill="none" stroke="#fff" stroke-width="2.5"/></svg></span>
  </div>
</section>

<div class="abs frame"></div>

<section>
  <div class="abs tag" style="left:127px;top:806px;width:158px">ABOUT US</div>
  <p class="abs copy" style="left:127px;top:866px;width:470px">Lorem ipsum dolor sit amet, consectetur adipiscing elit, sed do eiusmod tempor incididunt ut labore et dolore magna aliqua. Ut enim ad minim veniam, quis nostrud exercitation ullamco laboris nisi ut aliquip ex ea commodo consequat. Duis aute irure dolor in reprehenderit in voluptate velit esse cillum dolore eu fugiat nulla pariatur. Excepteur sint occaecat cupidatat non proident, sunt in culpa qui officia deserunt mollit anim id est laborum</p>
  <div class="abs btn btn-green" style="left:127px;top:1010px;width:120px;height:41px;font-size:14px">LEARN MORE</div>
  <div class="abs about-photo" role="img" aria-label="Photo of a businessman in a grey suit adjusting his tie"></div>
</section>

<section>
  <div class="abs banner" role="img" aria-label="Photo of an empty boardroom with a long table and chairs">
    <h2>START A BRIGHT CAREER AS A<br>SUCCESSFUL TRADER</h2>
  </div>
  <div class="abs join-outline">JOIN US</div>
</section>

<section>
  <div class="abs tag" style="left:127px;top:1531px;width:191px">WHAT WE DO</div>

  <article class="abs card" style="left:127px">
    <div class="card-head"><span class="card-num">1</span><span class="card-title">BEST SAVING PLANS</span></div>
    <p class="copy">dolor sit amet, consectetur adipiscing elit, sed do eiusmod tempor incididunt ut labore et dolore magna aliqua. Ut enim ad minim veniam, quis nostrud exercitation ullamco laboris nisi ut aliquip ex ea commodo consequat. Duis aute irure dolor in reprehenderit in voluptate velit esse cillum velit esse</p>
    <div class="btn btn-navy card-btn">LEARN MORE</div>
  </article>

  <article class="abs card active" style="left:453px">
    <div class="card-head"><span class="card-num">2</span><span class="card-title">FINANCIAL PLANS</span></div>
    <p class="copy">dolor sit amet, consectetur adipiscing elit, sed do eiusmod tempor incididunt ut labore et dolore magna aliqua. Ut enim ad minim veniam, quis nostrud exercitation ullamco laboris nisi ut aliquip ex ea commodo consequat. Duis aute irure dolor in reprehenderit in voluptate velit esse cillum velit esse</p>
    <div class="btn card-btn outline">LEARN MORE</div>
  </article>

  <article class="abs card" style="left:778px">
    <div class="card-head"><span class="card-num">3</span><span class="card-title">STUDY FEE PLANS</span></div>
    <p class="copy">dolor sit amet, consectetur adipiscing elit, sed do eiusmod tempor incididunt ut labore et dolore magna aliqua. Ut enim ad minim veniam, quis nostrud exercitation ullamco laboris nisi ut aliquip ex ea commodo consequat. Duis aute irure dolor in reprehenderit in voluptate velit esse cillum velit esse</p>
    <div class="btn btn-navy card-btn">LEARN MORE</div>
  </article>
</section>

<section>
  <div class="abs tag" style="left:127px;top:1982px;width:205px">WHY JOIN US?</div>
  <p class="abs copy" style="left:127px;top:2044px;width:392px;font-size:12px;line-height:17.5px">dolor sit amet, consectetur adipiscing elit, sed do eiusmod tempor incididunt ut labore et dolore magna aliqua. Ut enim ad minim veniam, quis nostrud exercitation ullamco laboris nisi ut aliquip ex ea commodo consequat. Duis aute irure dolor in reprehenderit in voluptate velit esse cillum</p>
  <ul class="abs bullets">
    <li>Best trading tips ever</li>
    <li>Secret tips from our experts</li>
    <li>We teach you how to trade online</li>
    <li>Learn how to trade commodities</li>
    <li>Learn how to become a trader</li>
  </ul>
  <div class="abs btn btn-green" style="left:127px;top:2276px;width:120px;height:41px;font-size:14px">LEARN MORE</div>
  <div class="abs head-font" style="left:276px;top:2286px;font-size:15px;font-weight:600;color:#333">OR</div>
  <div class="abs btn btn-navy" style="left:326px;top:2276px;width:120px;height:41px;font-size:14px">JOIN US</div>

  <form class="abs form-box">
    <div class="form-head">JOIN OUR SCHOOL NOW!</div>
    <div class="field" style="top:84px">First Name</div>
    <div class="field" style="top:132px">Last Name</div>
    <div class="field" style="top:180px">Email Address</div>
    <div class="agree"><i></i><span>Confirm that you are agree with <b>Terms &amp; Conditions</b></span></div>
    <div class="submit">SUBMIT</div>
  </form>
</section>

<footer class="abs footer">
  <div class="footer-brand"><span class="brand-dot"></span><span class="brand-name">Bramwelloq</span></div>
  <div class="footer-links"><span>Terms &amp; Conditions</span><span>|</span><span>Privacy Policy</span></div>
  <div class="footer-social"><span></span><span></span><span></span></div>
</footer>

</body>
</html>
```